Vesit cards for web development company

We need a business card design for our company. The company develops online platforms and conducts marketing consulting. Company logo. The cards must fit in with us (a junior start UP), but they must also be professional enough to impress with investors like banks. We wish you a combination of classic and modern design

Target Market(s)

Business partners and IT and marketing customers

Industry/Entity Type

It Company

Contact Information for Business Card

Folgende Information müssen Drauf.
Name, Position, Telefon Nr., Mobile Nr., E-Mail adresse, Optional sind noch Webadresse und HRB Nummer

Colors

Designer to choose colors to be used in the design.

Requirements
Must have
• The cards have to fit into the logo later and have to be dynamic and serious at the same time

```html
<!DOCTYPE html>
<html lang="en">
<head>
<meta charset="utf-8">
<title>Brightlane Development – Business Cards</title>
<link href="https://fonts.googleapis.com/css2?family=Montserrat:wght@400;600;700&display=swap" rel="stylesheet">
<style>
  :root{
    --brand-blue:#1273bf;
    --brand-grey:#8e8f93;
    --ink-grey:#6b6b6b;
    --paper:#ffffff;
    --backdrop:#eceef1;
  }
  *{box-sizing:border-box;margin:0;padding:0}
  html,body{width:1200px;height:1000px;overflow:hidden}
  body{background:var(--backdrop);font-family:"Montserrat",Arial,sans-serif;position:relative}

  .card{position:absolute;left:300px;width:600px;height:343px;background:var(--paper);
        box-shadow:0 8px 24px rgba(0,0,0,.15);overflow:hidden}
  .card--front{top:90px}
  .card--back{top:560px}

  /* wordmark */
  .wordmark{display:flex;align-items:center;gap:8px;color:var(--brand-blue);
            font-weight:700;letter-spacing:.5px}
  .wordmark__dot{width:14px;height:14px;border-radius:50%;background:var(--brand-blue);flex:none}

  /* front */
  .front__brand{position:absolute;left:36px;top:34px;font-size:20px}
  .front__person{position:absolute;left:60px;top:140px}
  .person__name{font-size:40px;font-weight:700;color:var(--brand-blue);letter-spacing:1px;line-height:1}
  .person__role{margin-top:8px;font-size:17px;font-weight:400;color:var(--ink-grey);text-align:right}

  .contact-panel{position:absolute;right:0;top:0;width:205px;height:100%;background:var(--brand-blue);padding:18px}
  .contact-panel__inner{width:100%;height:100%;background:var(--paper);outline:2px dashed var(--ink-grey);
        outline-offset:-8px;display:flex;flex-direction:column;justify-content:center;align-items:center;gap:14px}
  .contact-item{display:flex;flex-direction:column;align-items:center;gap:5px;font-size:12px;color:var(--ink-grey)}
  .contact-item svg{width:18px;height:18px;fill:var(--brand-blue)}
  .contact-item__badge{background:var(--brand-blue);color:var(--paper);font-size:9px;font-weight:600;padding:2px 4px}

  /* back */
  .back__band-top{position:absolute;left:0;top:0;width:100%;height:148px;background:var(--brand-blue)}
  .back__band-bottom{position:absolute;left:0;top:158px;width:100%;height:185px;background:var(--brand-grey)}
  .back__badge{position:absolute;left:190px;top:78px;width:220px;height:180px;background:var(--paper);
        display:flex;flex-direction:column;justify-content:center;align-items:center;gap:10px}
  .back__badge .wordmark{font-size:17px}
  .back__email{font-size:11px;color:var(--ink-grey);letter-spacing:1px}
</style>
</head>
<body>

<section class="card card--front">
  <div class="wordmark front__brand"><span class="wordmark__dot"></span>BRIGHTLANE</div>
  <div class="front__person">
    <h1 class="person__name">R.K HALDEN</h1>
    <p class="person__role">Senior Developer</p>
  </div>
  <div class="contact-panel">
    <div class="contact-panel__inner">
      <div class="contact-item">
        <svg viewBox="0 0 24 24"><path d="M7 2h10a2 2 0 0 1 2 2v16a2 2 0 0 1-2 2H7a2 2 0 0 1-2-2V4a2 2 0 0 1 2-2zm0 3v13h10V5zm5 14.2a1 1 0 1 0 0 .1z"/></svg>
        <span>+805-5550142</span>
      </div>
      <div class="contact-item">
        <svg viewBox="0 0 24 24"><path d="M2 5h20v14H2zm2 2v.5l8 5.5 8-5.5V7zm0 3v7h16v-7l-8 5.5z"/></svg>
        <span>hello@brightlane.dev</span>
      </div>
      <div class="contact-item">
        <svg viewBox="0 0 24 24"><path d="M12 2a10 10 0 1 0 0 20 10 10 0 0 0 0-20zm0 2c1 1.3 1.8 3.4 2 6h-4c.2-2.6 1-4.7 2-6zm-2.4.4A14 14 0 0 0 8 10H4.3a8 8 0 0 1 5.3-5.6zm4.8 0A8 8 0 0 1 19.7 10H16a14 14 0 0 0-1.6-5.6zM4.3 12H8a14 14 0 0 0 1.6 5.6A8 8 0 0 1 4.3 12zm5.7 0h4c-.2 2.6-1 4.7-2 6-1-1.3-1.8-3.4-2-6zm6 0h3.7a8 8 0 0 1-5.3 5.6A14 14 0 0 0 16 12z"/></svg>
        <span>brightlane.dev</span>
      </div>
      <div class="contact-item">
        <span class="contact-item__badge">123</span>
        <span>5005-4471203</span>
      </div>
    </div>
  </div>
</section>

<section class="card card--back">
  <div class="back__band-top"></div>
  <div class="back__band-bottom"></div>
  <div class="back__badge">
    <div class="wordmark"><span class="wordmark__dot"></span>BRIGHTLANE</div>
    <p class="back__email">hello@brightlane.dev</p>
  </div>
</section>

</body>
</html>
```